Lumaro Specs Needs Infographic Designs (Howto: Choose Your Lenses)

We need an infographic to explain to out customers on choosing their lenses. the file attached is the description and steps.

Would need your help to design an infograph which shows clearly the process and make the process looks easy.

You may use icons or graphics to better represent these information.

Colour scheme is orange, dark grey, white and black. My logo is orange in colour.

Target Market(s)

Age 18 to 35

Industry/Entity Type

Online

Font styles to use
Sans Serif
Decorative

Colors
f78f20
919191
eaeaea
000000

Requirements
Must have
• Must have good flow of information and represented with graphic.
Nice to have
• My project is nice to be simple to understand.
Should not have
• My project must not have alot of words.

```html
<!DOCTYPE html>
<html lang="en">
<head>
<meta charset="utf-8">
<title>Thin, Super Thin or Ultra Thin Lens?</title>
<link href="https://fonts.googleapis.com/css2?family=Roboto:ital,wght@0,400;0,700;0,900;1,700;1,900&display=swap" rel="stylesheet">
<style>
:root{
  --orange:#f78f20;
  --grey:#919191;
  --light:#eaeaea;
  --black:#000000;
  --dark:#3a3a3a;
  --white:#ffffff;
}
*{margin:0;padding:0;box-sizing:border-box}
html,body{width:841px;height:1200px;overflow:hidden;background:var(--white)}
body{font-family:"Roboto",Arial,sans-serif;color:var(--dark)}
.canvas{position:relative;width:841px;height:1200px;overflow:hidden}
.backdrop{position:absolute;inset:0;background:linear-gradient(180deg,#f1f1f1,#e4e4e4)}
.title-band{position:absolute;left:0;top:0;width:841px;height:58px;background:var(--orange);
  color:var(--white);font-weight:900;font-style:italic;font-size:38px;line-height:58px;text-align:center}
.tagline{position:absolute;left:60px;top:64px;width:721px;height:28px;background:var(--white);
  font-size:19px;line-height:28px;text-align:center;color:var(--dark)}
.steps-band{position:absolute;left:28px;top:104px;width:785px;height:36px;background:var(--dark);
  color:var(--white);font-weight:900;font-style:italic;font-size:28px;line-height:36px;text-align:center}
.step-badge{position:absolute;width:72px;height:72px;border-radius:50%;background:var(--grey);
  color:var(--white);font-weight:900;font-size:52px;line-height:72px;text-align:center}
.step-label{position:absolute;width:150px;font-size:21px;line-height:1.25;text-align:center;color:var(--dark)}
.glasses{position:absolute;left:336px;top:158px;width:170px;height:52px}
.divider{position:absolute;left:420px;top:236px;height:580px;border-left:4px dashed var(--grey)}
.card{position:absolute;background:var(--orange);border-radius:16px;color:var(--white);
  display:flex;align-items:center;font-size:21px;line-height:1.3}
.card .num{font-weight:900;font-size:92px;line-height:1;width:80px;text-align:center;flex:none}
.card .text{flex:1;text-align:center;padding:0 10px}
.card b{font-weight:900}
.note{position:absolute;left:470px;top:646px;width:342px;height:186px;background:var(--white);
  border:3px dashed var(--grey);border-radius:14px;font-size:21px;line-height:1.3;text-align:center;
  padding:18px 14px;color:var(--dark)}
.attr-title{position:absolute;left:28px;top:856px;width:392px;height:36px;background:var(--dark);
  color:var(--orange);font-weight:900;font-style:italic;font-size:24px;line-height:36px;padding-left:16px}
.attr-list{position:absolute;left:28px;top:900px;width:392px;list-style:none}
.attr-list li{display:flex;height:32px;margin-bottom:6px;background:var(--black);color:var(--white);
  font-size:18px;font-weight:700;line-height:32px}
.attr-list .idx{width:34px;background:var(--orange);text-align:center;font-weight:900;margin-right:10px}
.logo-spot{position:absolute;left:520px;top:1030px;font-size:52px;font-weight:400;color:var(--grey);letter-spacing:1px}
.foot-band{position:absolute;left:0;top:1168px;width:841px;height:32px;background:var(--orange)}
</style>
</head>
<body>
<main class="canvas">
  <div class="backdrop" role="img" aria-label="Soft grey background of faint spectacle outlines"></div>

  <h1 class="title-band">Thin, Super Thin or Ultra Thin Lens?</h1>
  <p class="tagline">Thinner lenses always make your spectacles look and fit better</p>
  <h2 class="steps-band">Choose your lenses in 2 easy steps!</h2>

  <div class="step-badge" style="left:34px;top:152px">1</div>
  <p class="step-label" style="left:120px;top:160px">Calculate your power</p>
  <div class="glasses" role="img" aria-label="Black spectacles icon">
    <svg width="170" height="52" viewBox="0 0 170 52">
      <rect x="4" y="8" width="66" height="40" rx="8" fill="none" stroke="var(--black)" stroke-width="7"/>
      <rect x="100" y="8" width="66" height="40" rx="8" fill="none" stroke="var(--black)" stroke-width="7"/>
      <path d="M70 20 Q85 10 100 20" fill="none" stroke="var(--black)" stroke-width="6"/>
    </svg>
  </div>
  <p class="step-label" style="left:566px;top:160px">Match your power with your lens</p>
  <div class="step-badge" style="left:736px;top:152px">2</div>

  <div class="divider"></div>

  <div class="card" style="left:28px;top:232px;width:364px;height:98px">
    <div class="text">Your prescription may look like this:<br><b>-2.50 / -1.50 x 150</b></div><div class="num">1</div>
  </div>
  <div class="card" style="left:28px;top:342px;width:364px;height:128px">
    <div class="text">Take the first power which is <b>2.50,</b> and add half of the second power <b>1.50.</b></div><div class="num">2</div>
  </div>
  <div class="card" style="left:28px;top:484px;width:364px;height:90px">
    <div class="text">The concluding power is <b>3.25!</b></div><div class="num">3</div>
  </div>
  <div class="card" style="left:28px;top:596px;width:364px;height:76px">
    <div class="text">Do the same for the other eye</div><div class="num">4</div>
  </div>
  <div class="card" style="left:28px;top:686px;width:364px;height:112px">
    <div class="text">If the signs are different, subtract the numbers from each other.</div><div class="num">5</div>
  </div>

  <div class="card" style="left:446px;top:232px;width:366px;height:98px">
    <div class="num">1</div><div class="text">Thin lenses are fitted by default. They are suitable for power below <b>4.00.</b></div>
  </div>
  <div class="card" style="left:446px;top:342px;width:366px;height:128px">
    <div class="num">2</div><div class="text">Thinner <b>1.67 index</b> lenses are recommended if your power is between <b>4.00 and 7.00</b></div>
  </div>
  <div class="card" style="left:446px;top:484px;width:366px;height:112px">
    <div class="num">3</div><div class="text">Thinnest <b>1.74 index</b> lenses are recommended if your power is above <b>7.00.</b></div>
  </div>

  <p class="note">You may choose lenses thinner or thicker than recommended but keep in mind thinner lenses always make your spectacles look and fit better!</p>

  <h3 class="attr-title">Attributes of our Lenses</h3>
  <ul class="attr-list">
    <li><span class="idx">1</span>Aspheric design – for sharper vision</li>
    <li><span class="idx">2</span>UV and blue light protection</li>
    <li><span class="idx">3</span>Multicoated Scratch Resistance</li>
    <li><span class="idx">4</span>Lightweight technology</li>
  </ul>

  <p class="logo-spot">YOUR LOGO</p>
  <div class="foot-band"></div>
</main>
</body>
</html>
```